Web Design Project - ClipHaven Style Website

Hi there, we want to create a ClipHaven / Falzo style website. We have a logo, and will be using a similar structure to this platform; http://reelpail.example/v2/
Please feel free to be creative as possible, and make the site look however you would like :) keeping in mind the Ad space, and user friendly layout. We would like
1) The main page and
2) the video view page
designed
Logo, and images attached
Updates
Logo and stock image uploaded
Hello; we most likely be basing the site on this reel pail theme, which also works as a mobile version.
Another option that I found for a layout which is different :)
http://www.quarnet-studio.example/demo-theme.cfm?theme=pivota
One last update; really like this one too
I am 100% likely to now use this format;
Target Market(s)
Bars, Cafe's, Restaurants, Attractions, Venues, Pubs, Wine and Dine
Industry/Entity Type
Cliphaven
Requirements
Must have
- Can be similar to ClipHaven, but closer to Falzo's funky fresh look.
Should not have
- Not be too cluttered with too many videos on the home page. Feel free to think outside the box

```html
<!DOCTYPE html>
<html lang="en">
<head>
<meta charset="utf-8">
<title>Riverton Reels — Home</title>
<link rel="stylesheet" href="https://fonts.googleapis.com/css2?family=Arimo:wght@400;700&display=swap">
<style>
:root{
  --header-mid:#3b3b40;
  --header-stripe:#c9cbd3;
  --nav-text:#ececec;
  --ink:#1c1c1c;
  --frame:#2b2b2e;
  --ribbon-top:#5a5a5f;
  --ribbon-bottom:#38383c;
  --progress:#7fc9ef;
  --progress-buffer:#3b4a57;
  --ad-green:#adbb78;
  --white:#ffffff;
}
*{box-sizing:border-box;margin:0;padding:0}
html,body{width:1111px;height:1200px;overflow:hidden;background:var(--white)}
body{position:relative;font-family:"Arimo",Arial,sans-serif;color:var(--ink)}

.site-header{position:absolute;left:0;top:0;width:1111px;height:84px;
  background:linear-gradient(180deg,#505056 0%,var(--header-mid) 100%)}
.site-header::after{content:"";position:absolute;left:0;top:84px;width:100%;height:12px;
  background:linear-gradient(180deg,#a9abb4,var(--header-stripe) 40%,#e4e5ea)}
.brand{position:absolute;left:81px;top:20px;display:flex;align-items:center;gap:12px;
  color:var(--white);font-size:38px;font-weight:700;letter-spacing:-.5px}
.brand-mark{width:14px;height:14px;background:var(--white)}
.main-nav{position:absolute;right:84px;top:60px;display:flex;gap:18px}
.main-nav a{color:var(--nav-text);text-decoration:none;font-size:15.5px;font-weight:700}

.feature{position:absolute;left:83px;top:118px;width:946px;height:533px;background:var(--frame);
  border:1px solid #1a1a1a}
.feature-media{position:absolute;left:0;top:18px;width:944px;height:514px;
  background:linear-gradient(180deg,#76859b 0%,#a7b2bc 28%,#d9d2b2 48%,#f3bf47 68%,#ea7d1d 74%,#3a3431 80%,#2a2a2c 100%)}
.feature-ribbon{position:absolute;left:-12px;top:17px;width:970px;height:43px;
  background:linear-gradient(180deg,var(--ribbon-top),var(--ribbon-bottom));
  box-shadow:0 2px 4px rgba(0,0,0,.4);color:var(--white);font-size:24px;font-weight:400;
  padding:8px 0 0 18px;white-space:nowrap}
.feature-ribbon strong{font-weight:700;margin-right:10px}
.feature-ribbon::before,.feature-ribbon::after{content:"";position:absolute;bottom:-9px;
  border-top:9px solid #1e1e20}
.feature-ribbon::before{left:0;border-left:12px solid transparent}
.feature-ribbon::after{right:0;border-right:12px solid transparent}

.player-controls{position:absolute;left:194px;top:461px;width:554px;height:45px;
  background:rgba(25,25,28,.92);border:1px solid #444;border-radius:3px}
.player-controls svg{position:absolute;left:0;top:0}
.player-time{position:absolute;left:421px;top:14px;color:#eee;font-size:13px;line-height:16px}
.player-hd{position:absolute;left:474px;top:13px;color:var(--progress);font-size:14px;line-height:17px;font-weight:700}

.section-title{position:absolute;left:81px;font-size:31px;font-weight:400}
.section-title.featured{top:672px}
.section-title.recent{top:955px}

.thumb{position:absolute;width:185px;height:105px;border:1px solid #222}
.thumb svg{position:absolute;left:83px;top:43px}
.row-featured .thumb{top:717px}
.row-recent .thumb{top:998px}

.intro{position:absolute;left:81px;top:844px;width:569px;font-size:15.5px;line-height:20px;text-align:justify}
.intro strong{font-size:18px}

.ad-slot{position:absolute;left:727px;top:717px;width:240px;height:240px;background:var(--ad-green);
  border:1px solid #97a566;color:var(--white);font-size:31px;line-height:28px;padding:32px 0 0 18px}

.site-footer{position:absolute;right:87px;top:1141px;font-size:12px;color:#222}
.site-footer strong{font-weight:700}
</style>
</head>
<body>
<header class="site-header">
  <div class="brand"><span class="brand-mark"></span>Riverton Reels</div>
  <nav class="main-nav">
    <a href="#">Search</a><a href="#">Featured Videos</a><a href="#">Recent Videos</a>
    <a href="#">Top Channels</a><a href="#">Register</a><a href="#">Login</a>
  </nav>
</header>

<section class="feature">
  <div class="feature-media" role="img" aria-label="Timelapse still: aircraft wing silhouetted against a sunset sky over clouds"></div>
  <h1 class="feature-ribbon"><strong>FETURED:</strong>SF to Paris flight timelapse</h1>
  <div class="player-controls">
    <svg width="554" height="45" viewBox="0 0 554 45">
      <path d="M22 14 L36 22 L22 30 Z" fill="#fff"/>
      <path d="M70 18 H74 L80 13 V31 L74 26 H70 Z" fill="#fff"/>
      <path d="M83 17 V27 M86 15 V29 M89 18 V26" stroke="#fff" stroke-width="1.5"/>
      <rect x="106" y="17" width="298" height="10" rx="5" fill="#111" stroke="#444"/>
      <rect x="107" y="18" width="184" height="8" rx="4" fill="var(--progress-buffer)"/>
      <rect x="107" y="18" width="139" height="8" rx="4" fill="var(--progress)"/>
      <path d="M518 31 L525 24 M518 31 V26 M518 31 H523 M536 13 L529 20 M536 13 V18 M536 13 H531" stroke="#fff" stroke-width="2.2" fill="none"/>
    </svg>
    <span class="player-time">11:57</span>
    <span class="player-hd">HD</span>
  </div>
</section>

<h2 class="section-title featured">Other featured videos:</h2>
<div class="row-featured">
  <div class="thumb" style="left:83px;background:linear-gradient(180deg,#3d74c6,#9cc0e4 55%,#1f3e55)" role="img" aria-label="City skyline across a river with hot air balloons"><svg width="16" height="18"><path d="M2 1 L15 9 L2 17 Z" fill="#fff"/></svg></div>
  <div class="thumb" style="left:274px;background:linear-gradient(160deg,#2a2a2e,#6d8fb6 55%,#d8c4a5)" role="img" aria-label="Chef plating dishes on a restaurant table"><svg width="16" height="18"><path d="M2 1 L15 9 L2 17 Z" fill="#fff"/></svg></div>
  <div class="thumb" style="left:466px;background:linear-gradient(180deg,#1e1814,#5a3a2a 55%,#2a1c16)" role="img" aria-label="Bar interior with lamps and bottle shelves"><svg width="16" height="18"><path d="M2 1 L15 9 L2 17 Z" fill="#fff"/></svg></div>
</div>

<p class="intro"><strong>Riverton Reels</strong>, is a video sharing site that lorem ipsum dolor sit amet, consectetur adipiscing elit. In porta, ante et molestie tincidunt, enim massa porta nibh, eget fermentum neque tellus eu tortor. Morbi sit amet lorem orci. Sed sit amet leo eget nibh volutpat elementum sagittis id ante. In accumsan ipsum id quam ornare a viverra elit blandit.</p>

<aside class="ad-slot">advertisement space :)</aside>

<h2 class="section-title recent">Most recent videos:</h2>
<div class="row-recent">
  <div class="thumb" style="left:83px;background:linear-gradient(160deg,#d9d4c6,#e5c94a 45%,#6b6a5f)" role="img" aria-label="Bright retail store interior"><svg width="16" height="18"><path d="M2 1 L15 9 L2 17 Z" fill="#fff"/></svg></div>
  <div class="thumb" style="left:273px;background:linear-gradient(180deg,#2c2a22,#7b6a4c 55%,#3fa2a8)" role="img" aria-label="Hotel courtyard with pool at dusk"><svg width="16" height="18"><path d="M2 1 L15 9 L2 17 Z" fill="#fff"/></svg></div>
  <div class="thumb" style="left:463px;background:linear-gradient(160deg,#3a2418,#8a5a3a 55%,#d8cdbd)" role="img" aria-label="Hotel bedroom interior"><svg width="16" height="18"><path d="M2 1 L15 9 L2 17 Z" fill="#fff"/></svg></div>
  <div class="thumb" style="left:653px;background:linear-gradient(180deg,#3c2a20,#8a7358 55%,#2e2019)" role="img" aria-label="Ornate grand staircase in a heritage lobby"><svg width="16" height="18"><path d="M2 1 L15 9 L2 17 Z" fill="#fff"/></svg></div>
  <div class="thumb" style="left:844px;background:linear-gradient(160deg,#c9cfd6,#eeeeee 45%,#b83a3a 80%,#5d5f63)" role="img" aria-label="Tourist shuttle bus parked at a stop"><svg width="16" height="18"><path d="M2 1 L15 9 L2 17 Z" fill="#fff"/></svg></div>
</div>

<footer class="site-footer">Copyright © 2012 - 2013 &nbsp;<strong>rivertonreels.example</strong></footer>
</body>
</html>
```